Corvane

I'm looking for business cards with the logo I've attached. I don't have an specific idea in mind and open to anything. All the usual info will be involved. Name, position in company, nr, email, address

```html
<!DOCTYPE html>
<html lang="en">
<head>
<meta charset="utf-8">
<title>Corvane Designs – Business Card</title>
<link href="https://fonts.googleapis.com/css2?family=Montserrat:wght@400;500;600;700&display=swap" rel="stylesheet">
<style>
  :root {
    --gold: #e2a03e;
    --gold-deep: #d18f2c;
    --navy: #1b2944;
    --paper: #ffffff;
    --ink: #1f2a40;
    --backdrop: #c9cccd;
  }
  * { margin: 0; padding: 0; box-sizing: border-box; }
  html, body {
    width: 1200px; height: 928px; overflow: hidden;
    background: var(--backdrop);
    font-family: "Montserrat", sans-serif;
  }
  .canvas { position: relative; width: 1200px; height: 928px; }

  .card {
    position: absolute;
    left: 265px;
    width: 672px;
    height: 384px;
    overflow: hidden;
    box-shadow: 0 10px 24px rgba(0,0,0,0.25);
  }
  .card--front { top: 58px; background: var(--gold); }
  .card--back  { top: 484px; background: var(--paper); }

  /* Wordmark */
  .wordmark { position: absolute; text-align: center; font-weight: 600; line-height: 1; }
  .wordmark__name { display: block; text-transform: uppercase; }
  .wordmark__sub  { display: block; text-transform: uppercase; }

  .card--front .wordmark {
    left: 0; right: 0; top: 214px; color: var(--gold-deep);
  }
  .card--front .wordmark__name { font-size: 56px; letter-spacing: 0.02em; }
  .card--front .wordmark__sub  { font-size: 24px; letter-spacing: 0.62em; margin-top: 14px; padding-left: 0.62em; }

  .card--back .wordmark {
    left: 370px; width: 270px; top: 212px; color: var(--gold);
  }
  .card--back .wordmark__name { font-size: 42px; letter-spacing: 0.01em; }
  .card--back .wordmark__sub  { font-size: 18px; letter-spacing: 0.6em; margin-top: 12px; padding-left: 0.6em; }

  /* Contact block */
  .contact { position: absolute; left: 53px; top: 72px; color: var(--ink); }
  .contact__name {
    font-size: 20px; font-weight: 700; color: var(--gold);
    letter-spacing: 0.03em; text-transform: uppercase;
  }
  .contact__role { font-size: 15px; font-weight: 500; margin-top: 8px; }
  .contact__address { font-size: 15px; font-weight: 500; line-height: 24px; margin-top: 42px; }
  .contact__list { list-style: none; margin-top: 40px; font-size: 15px; font-weight: 500; }
  .contact__list li { display: flex; align-items: center; height: 24px; }
  .contact__icon { width: 13px; height: 13px; margin-right: 6px; fill: var(--gold); flex: none; }

  .card__stripe { position: absolute; left: 0; bottom: 0; width: 672px; height: 14px; }
</style>
</head>
<body>
<main class="canvas">

  <section class="card card--front" aria-label="Card front">
    <div class="wordmark">
      <span class="wordmark__name">Corvane</span>
      <span class="wordmark__sub">Designs</span>
    </div>
  </section>

  <section class="card card--back" aria-label="Card back">
    <div class="contact">
      <p class="contact__name">Julien Marchand</p>
      <p class="contact__role">Business Development</p>
      <p class="contact__address">41B Ridgeview Way NE,<br>Calgary, AB T2K 3R5</p>
      <ul class="contact__list">
        <li>
          <svg class="contact__icon" viewBox="0 0 16 16" aria-hidden="true"><path d="M3.6 1.2l2.3 2.6-1.3 1.9c.9 2 2.5 3.6 4.5 4.6l1.9-1.3 2.6 2.3-1.4 2.8C6.8 14 2 9.2 .9 3z"/></svg>
          (555) 214-7390
        </li>
        <li>
          <svg class="contact__icon" viewBox="0 0 16 16" aria-hidden="true"><path d="M1 3h14v1.2L8 8.6 1 4.2z"/><path d="M1 5.6l7 4.4 7-4.4V13H1z"/></svg>
          info@corvanedesigns.ca
        </li>
        <li>
          <svg class="contact__icon" viewBox="0 0 16 16" aria-hidden="true"><circle cx="8" cy="8" r="7"/><path d="M4 5.5c1.5-.5 2.5.5 3 1.5s-.5 2 .5 3-.5 2.5-1 3M10 3c-.5 1 0 2 1 2.3s2 1.2 1.8 2.5" stroke="#fff" stroke-width="1.1" fill="none"/></svg>
          www.corvanedesigns.ca
        </li>
      </ul>
    </div>

    <div class="wordmark">
      <span class="wordmark__name">Corvane</span>
      <span class="wordmark__sub">Designs</span>
    </div>

    <svg class="card__stripe" viewBox="0 0 672 14" preserveAspectRatio="none" aria-hidden="true">
      <rect x="0" y="7" width="526" height="7" fill="var(--navy)"/>
      <polygon points="532,14 546,0 672,0 672,14" fill="var(--gold)"/>
    </svg>
  </section>

</main>
</body>
</html>
```